Re-design my 1-page website to be BETTER!

Hi Guys,
I recently created a 1-page website for market testing purposes for a company I am starting. Problem is, the feedback i've had on the page is its a bit corporate and boring.
I would love you to design something that is fresher, more modern and will generate leads (via the sign up CTA's).
Here is the website as it is now: www.guidelinkhub.com.au.
If you need any info or have questions, just reach out.
Thanks,
Oliver

Target Market(s)

Entrepreneurs

Number of Pages Required

1 page

Font styles to use
Sans Serif

Colors
abd036
34a6d7
ffffff

Requirements
Must have
• Fresh, Modern, high-converting
• I expect 70% of traffic to be mobile so must be mobile optimised first.
Nice to have
• I've highlighted colours i like below, however, I am open to suggestions. I like colours that are gender neutral and show energy and vibrancy.
• I have used Proxima Nova for the fonts, as I find it easy to read however, I am open to suggestions. My main preference is that it displays well and is easily read

```html
<!DOCTYPE html>
<html lang="en">
<head>
<meta charset="utf-8">
<title>GuideLink Hub — A Mentor For Everyone</title>
<link href="https://fonts.googleapis.com/css2?family=Montserrat:wght@400;500;600;700&family=Open+Sans:ital,wght@0,400;0,600;1,400&display=swap" rel="stylesheet">
<style>
:root{
  --green:#8dc63f;
  --blue:#34a6d7;
  --ink:#333a40;
  --body:#6d7378;
  --muted:#8a9095;
  --pale:#eef2f2;
  --white:#ffffff;
}
*{margin:0;padding:0;box-sizing:border-box}
html,body{width:1200px;height:3774px;overflow:hidden}
body{position:relative;background:var(--white);font-family:"Open Sans",Arial,sans-serif;color:var(--body)}
.abs{position:absolute}
.section{position:absolute;left:0;width:1200px}
h1,h2,h3,h4,.logo,.nav a,.btn{font-family:"Montserrat",Arial,sans-serif}
h2{font-size:20px;font-weight:600;letter-spacing:2px;color:var(--ink);text-transform:uppercase;line-height:28px}
.rule{position:absolute;height:2px;background:var(--blue);width:62px}
p{font-size:9px;line-height:18.6px}
.btn{position:absolute;display:flex;align-items:center;justify-content:center;background:var(--blue);color:var(--white);font-size:8px;font-weight:700;letter-spacing:1px;text-transform:uppercase;text-decoration:none}
.fine{position:absolute;font-size:7.5px;color:var(--muted);font-family:"Montserrat",Arial,sans-serif}

/* hero */
.hero{top:0;height:587px;background:linear-gradient(100deg,#8f8a86 0%,#6f7276 35%,#84868a 60%,#5c6167 100%)}
.hero-shade{position:absolute;inset:0;background:rgba(40,44,50,.35)}
.logo{left:103px;top:27px;font-size:17px;font-weight:600;color:var(--white)}
.nav{position:absolute;top:29px;left:0;width:1200px}
.nav a{position:absolute;color:var(--white);font-size:10px;font-weight:500;text-decoration:none}
.nav .cta{left:1009px;top:-9px;width:87px;height:31px;border:2px solid var(--white);border-radius:16px;display:flex;align-items:center;justify-content:center;font-size:8px;font-weight:700;letter-spacing:1px}
.hero h1{left:0;width:1200px;top:178px;text-align:center;font-size:35px;font-weight:500;color:var(--white)}
.hero .quote{left:0;width:1200px;top:242px;text-align:center;font-style:italic;font-size:15.5px;line-height:25px;color:var(--white)}
.hero .by{left:0;width:1200px;top:304px;text-align:center;font-size:11px;color:#e8e8e8;font-family:"Montserrat",Arial,sans-serif}
.hero .fine{left:0;width:1200px;top:399px;text-align:center;color:#eee}

/* intro */
.intro{top:587px;height:537px}
.photo{position:absolute}
.intro .col{left:653px;width:315px}
.intro p{color:var(--body);margin-bottom:7px}

/* different */
.different{top:1124px;height:657px;background:var(--pale)}
.card{position:absolute;top:194px;width:231px;height:291px;background:var(--white)}
.card svg{position:absolute;left:25px;top:44px}
.card h4{position:absolute;left:25px;top:112px;font-size:10px;font-weight:700;letter-spacing:.6px;color:var(--ink);text-transform:uppercase}
.card .rule{left:25px;top:141px;width:44px}
.card p{position:absolute;left:25px;top:158px;width:186px}

/* how */
.how{top:1781px;height:642px}
.step{position:absolute;width:235px}
.step .icon{position:absolute;left:0;top:0;width:44px;height:44px;background:var(--green);display:flex;align-items:center;justify-content:center}
.step h4{position:absolute;left:62px;top:0;font-size:12px;font-weight:500;color:var(--ink)}
.step p{position:absolute;left:62px;top:24px;width:172px}
.btn.outline{background:transparent;border:2px solid var(--green);color:var(--ink)}

/* faq */
.faq{top:2423px;height:844px;background:var(--pale)}
.faq h2{position:absolute;left:0;width:1200px;text-align:center;font-size:20px}
.q{position:absolute;left:359px;width:481px;height:32px;background:var(--white);border-radius:3px;display:flex;align-items:center;padding-left:22px;font-size:10px;color:var(--ink)}
.q svg{position:absolute;right:18px;top:12px}
.answer{position:absolute;left:381px;width:445px}
.answer p{margin-bottom:19px}

/* invest */
.invest{top:3267px;height:507px;background:linear-gradient(95deg,#4d4440 0%,#5d4b43 30%,#7a6a61 55%,#a59a93 75%,#46413e 100%)}
.invest .shade{position:absolute;inset:0;background:linear-gradient(90deg,rgba(20,20,25,.55) 0%,rgba(20,20,25,.25) 55%,rgba(0,0,0,0) 100%)}
.invest h2{color:var(--white)}
.invest p{color:#eee;margin-bottom:18px}
.invest .fine{color:#ddd}
</style>
</head>
<body>

<header class="section hero">
  <div class="abs" style="inset:0" role="img" aria-label="Photo of two professionals shaking hands in a bright brick-walled office"></div>
  <div class="hero-shade"></div>
  <div class="logo abs">GuideLinkHub</div>
  <nav class="nav">
    <a style="left:713px" href="#about">About</a>
    <a style="left:776px" href="#mentorship">Mentorship</a>
    <a style="left:864px" href="#how">How it works</a>
    <a style="left:960px" href="#faq">FAQ</a>
    <a class="cta" href="#signup">SIGN UP</a>
  </nav>
  <h1 class="abs">A Mentor For Everyone</h1>
  <div class="quote abs">"We've flipped the model on its head -  so now you choose your Mentor.  It's never been this<br>easy to get the advice and guidance you need to thrive"</div>
  <div class="by abs">Oliver, Founder - GuideLink Hub</div>
  <a class="btn" style="left:542px;top:349px;width:116px;height:38px" href="#signup">Sign up now</a>
  <div class="fine">Register Free. 100% confidential. Obligation Free</div>
</header>

<section class="section intro" id="about">
  <div class="photo" style="left:234px;top:87px;width:356px;height:362px;background:linear-gradient(135deg,#8a4e38 0%,#6a5a52 40%,#5b6f86 65%,#8a7b6a 100%)" role="img" aria-label="Photo of an older mentor and a young man working together at a desk"></div>
  <h2 class="abs" style="left:653px;top:97px;width:320px">Finding a mentor has<br>never been easier</h2>
  <div class="rule" style="left:653px;top:160px"></div>
  <div class="col abs" style="top:180px">
    <p>Having a great Mentor will turbo-charge your personal, professional or business growth.  But unless you have an incredible network, finding great Mentors has always been a challenge.</p>
    <p>GuideLink Hub changes all that, levelling the playing field and making it easy for entrepreneurs and professionals to find the advice and guidance they deserve.</p>
    <p>No longer will you have to go searching for your perfect Mentor.  We bring the perfect Mentor to you, selected from a global pool of experts, putting the power back in your hands and letting you get on with your growth.</p>
  </div>
  <a class="btn" style="left:653px;top:390px;width:104px;height:34px" href="#signup">Sign up now</a>
  <div class="fine" style="left:653px;top:435px">Register Free. 100% confidential. Obligation Free</div>
</section>

<section class="section different" id="mentorship">
  <h2 class="abs" style="left:234px;top:79px">Mentorship: but different</h2>
  <div class="rule" style="left:234px;top:124px"></div>
  <p class="abs" style="left:234px;top:144px">Finding a Mentor used to be hard; but not any more. We've turned the traditional model on its head, so now Mentors seek you.</p>

  <div class="card" style="left:234px">
    <svg width="38" height="38" viewBox="0 0 38 38" fill="none" stroke="#34a6d7" stroke-width="1.3"><rect x="6" y="4" width="26" height="16"/><line x1="10" y1="9" x2="28" y2="9"/><line x1="10" y1="14" x2="22" y2="14"/><line x1="2" y1="28" x2="36" y2="28"/><line x1="8" y1="28" x2="8" y2="36"/><line x1="30" y1="28" x2="30" y2="36"/></svg>
    <h4>Tell us what you need</h4>
    <div class="rule"></div>
    <p>There is no one size fits all approach to Mentorship.  So tell us the challenges you are facing and the skill-set your Mentor must have.</p>
  </div>
  <div class="card" style="left:485px">
    <svg width="38" height="38" viewBox="0 0 38 38" fill="none" stroke="#34a6d7" stroke-width="1.3"><circle cx="19" cy="9" r="6"/><polyline points="16,9 18.5,11.5 22.5,6.5"/><rect x="3" y="22" width="8" height="8"/><rect x="15" y="22" width="8" height="8"/><rect x="27" y="22" width="8" height="8"/><line x1="1" y1="34" x2="37" y2="34"/></svg>
    <h4>Choose your mentor</h4>
    <div class="rule"></div>
    <p>Mentors are invited to Mentor you. We select 3 top picks that align with your criteria.  It's then up to you whether you choose a Mentor, interview 1 or more or refine your criteria and start again.</p>
  </div>
  <div class="card" style="left:734px">
    <svg width="38" height="38" viewBox="0 0 38 38" fill="none" stroke="#34a6d7" stroke-width="1.3"><path d="M8 20a11 11 0 0 1 22 0"/><rect x="5" y="18" width="5" height="8" rx="1"/><rect x="28" y="18" width="5" height="8" rx="1"/><path d="M30 26q0 6-8 6"/><line x1="3" y1="36" x2="35" y2="36"/></svg>
    <h4>Ongoing support</h4>
    <div class="rule"></div>
    <p>We don't stop once you have your perfect Mentor.  We're on hand to make life easy for you, keep your sessions on track and provide ongoing support.</p>
  </div>

  <a class="btn" style="left:234px;top:517px;width:104px;height:34px" href="#signup">Sign up now</a>
  <div class="fine" style="left:234px;top:562px">Register Free. 100% confidential. Obligation Free</div>
</section>

<section class="section how" id="how">
  <h2 class="abs" style="left:234px;top:86px">How it works</h2>

  <div class="step" style="left:234px;top:165px">
    <div class="icon"><svg width="22" height="22" viewBox="0 0 22 22" fill="none" stroke="#fff" stroke-width="1.4"><polyline points="3,12 8,17 19,5"/></svg></div>
    <h4>Impartial advice</h4>
    <p>Imagine being able to speak to someone who has been through the challenges you are currently facing?  Who has "been there seen that" and can help you navigate the ups and downs of your career?</p>
  </div>
  <div class="step" style="left:483px;top:165px">
    <div class="icon"><svg width="22" height="22" viewBox="0 0 22 22" fill="none" stroke="#fff" stroke-width="1.4"><path d="M11 2l8 4v6c0 4-4 7-8 8-4-1-8-4-8-8V6z"/></svg></div>
    <h4>Avoid the Pitfalls</h4>
    <p>An experienced Mentor will help you see the challenges before they arise and make sure you avoid them altogether.  Saving valuable time and money in the process.</p>
  </div>
  <div class="step" style="left:734px;top:165px">
    <div class="icon"><svg width="22" height="22" viewBox="0 0 22 22" fill="none" stroke="#fff" stroke-width="1.4"><path d="M3 4h16v10H9l-4 4v-4H3z"/></svg></div>
    <h4>A Supportive Ear</h4>
    <p>Running a business and the challenges of corporate life can be extremely stressful.  So imagine having someone independent who can understand where your coming from and, help you see things objectively.</p>
  </div>
  <div class="step" style="left:234px;top:322px">
    <div class="icon"><svg width="22" height="22" viewBox="0 0 22 22" fill="none" stroke="#fff" stroke-width="1.4"><circle cx="9" cy="9" r="6"/><line x1="13.5" y1="13.5" x2="19" y2="19"/></svg></div>
    <h4>Clarity</h4>
    <p>Sometimes we are so caught up in our own world we struggle to see the big picture.  You Mentor will provide an objective, outsider view.  Helping you to cut though the noise and focus on what's really important.</p>
  </div>
  <div class="step" style="left:483px;top:322px">
    <div class="icon"><svg width="22" height="22" viewBox="0 0 22 22" fill="none" stroke="#fff" stroke-width="1.4"><polyline points="3,16 8,11 12,14 19,6"/><polyline points="14,6 19,6 19,11"/></svg></div>
    <h4>Motivation</h4>
    <p>Your Mentor has seen this before and been in your shoes.  They understand what your going through and will help you to re-focus and re-energise.</p>
  </div>
  <div class="step" style="left:734px;top:322px">
    <div class="icon"><svg width="22" height="22" viewBox="0 0 22 22" fill="none" stroke="#fff" stroke-width="1.4"><rect x="4" y="3" width="14" height="17"/><polyline points="7,9 9,11 12,7"/><line x1="7" y1="15" x2="15" y2="15"/></svg></div>
    <h4>Make you Accountable</h4>
    <p>A Mentor is not just there to pick you up - they are to give honest appraisal and tell you when your falling short.  Ultimately, only you can control your success and you Mentor will hold you accountable to make sure you are.</p>
  </div>

  <a class="btn outline" style="left:296px;top:503px;width:104px;height:33px" href="#signup">Sign up now</a>
  <div class="fine" style="left:296px;top:548px">Register Free. 100% confidential. Obligation Free</div>
</section>

<section class="section faq" id="faq">
  <h2 style="top:80px">Frequently asked questions</h2>
  <div class="rule" style="left:547px;top:120px;width:107px"></div>

  <div class="q" style="top:161px">What is a Mentor?<svg width="10" height="7" viewBox="0 0 10 7" fill="none" stroke="#8a9095" stroke-width="1.2"><polyline points="1,6 5,2 9,6"/></svg></div>
  <div class="answer" style="top:209px">
    <p>Experienced and Trusted Advisor.  Guru.  Confidente.  Friend.</p>
    <p>In essence a Mentor is someone who can turn to for guidance and advice.</p>
    <p>Someone who is more experienced than you and, has navigated similar challenges to you and can foresee the pitfalls and hurdles you face.</p>
    <p>A great Mentor is also a motivator, connector and guide.  Will help you focus on what's really important and see the bigger picture.</p>
    <p>Importantly, a great Mentor should be outside your immediate network of friends and relatives.  And, be able to offer unbiased, honest and objective advice, that you can action.</p>
  </div>

  <div class="q" style="top:469px">Is a Mentor right for me?<svg width="10" height="7" viewBox="0 0 10 7" fill="none" stroke="#8a9095" stroke-width="1.2"><polyline points="1,1 5,5 9,1"/></svg></div>
  <div class="q" style="top:520px">How often do we meet?<svg width="10" height="7" viewBox="0 0 10 7" fill="none" stroke="#8a9095" stroke-width="1.2"><polyline points="1,1 5,5 9,1"/></svg></div>
  <div class="q" style="top:572px">Can I have more than one Mentor?<svg width="10" height="7" viewBox="0 0 10 7" fill="none" stroke="#8a9095" stroke-width="1.2"><polyline points="1,1 5,5 9,1"/></svg></div>
  <div class="q" style="top:623px">What if it doesn't work out?<svg width="10" height="7" viewBox="0 0 10 7" fill="none" stroke="#8a9095" stroke-width="1.2"><polyline points="1,1 5,5 9,1"/></svg></div>
  <div class="q" style="top:674px">How do we meet?<svg width="10" height="7" viewBox="0 0 10 7" fill="none" stroke="#8a9095" stroke-width="1.2"><polyline points="1,1 5,5 9,1"/></svg></div>
  <div class="q" style="top:725px">What are the costs?<svg width="10" height="7" viewBox="0 0 10 7" fill="none" stroke="#8a9095" stroke-width="1.2"><polyline points="1,1 5,5 9,1"/></svg></div>
</section>

<section class="section invest" id="signup">
  <div class="abs" style="inset:0" role="img" aria-label="Photo of two women working together at a computer in a brick-walled office"></div>
  <div class="shade"></div>
  <h2 class="abs" style="left:234px;top:118px">It's time to invest in you</h2>
  <div class="rule abs" style="left:234px;top:166px;background:#fff"></div>
  <div class="abs" style="left:234px;top:188px;width:300px">
    <p>If you've come this far you've already taken the most important step; recognising how mentorship can help you; and taking action to find it.</p>
    <p>And now your here, the rest is easy.</p>
    <p>Get started now and let GuideLink Hub do the rest...</p>
  </div>
  <a class="btn" style="left:234px;top:321px;width:104px;height:33px" href="#">Sign up now</a>
  <div class="fine" style="left:234px;top:366px">Register Free. 100% confidential. Obligation Free</div>
</section>

</body>
</html>
```